Premium CBD/Hemp company needs packaging and label design

Verdant Oakfield, a premium CBD/Hemp company based in Scottsdale, Arizona is in need of a packaging and label design. We are launching with our flagship product which will be a 30 count capsule and will come in three functions: Pain Relief, Anxiety Support, and Sleep Support. For the purpose of this contest, please design packaging and label for our Anxiety Support product. Our products are physician formulated and all natural. Our main ingredient is CBD/Hemp and is complemented by specific herbs that synergistically work together to give the customer the most effective and desired result. We would like our branding to have a pharmaceutical look and feel with a focus on trust and transparency. We have uploaded our company logo that is to be used on both the packaging and label. We have also uploaded an executed branding questionnaire that will guide you to exactly what we are seeking to achieve as to the look and feel of our brand. Please feel free to contact us with any questions that you may have. The winner of this contest will have the opportunity to work with us on future projects as we will need packaging and label design for our entire Verdant Oakfield product line.

Target Market(s)

See attached branding questionnaire

Industry/Entity Type

Health And Wellness

Font styles to use
Sans Serif

Colors

Designer to choose colors to be used in the design.

Requirements
Must have
• See attached branding questionnaire; Please superimpose labels onto a cobalt blue capsule bottle (see attached)
• >>UPON REVIEW of the FIRST 8 designs, we really like the silver, mildly metallic label background in DESIGN # 21300528, we do not want metalic lettering as that would not look very "Pharmaceutical"
• >>We are in search of a look that is a bit more "Pharmaceutical" than a look that would be more commonly found in a Supplement Store
Nice to have
• "See attached branding questionnaire
Should not have
• See attached branding questionnaire; NO marijuana or cannabis plant on the packaging or label

```html
<!DOCTYPE html>
<html lang="en">
<head>
<meta charset="utf-8">
<title>Verdant Oakfield – Anxiety Support packaging</title>
<link rel="stylesheet" href="https://fonts.googleapis.com/css2?family=Encode+Sans+Condensed:wght@300;400&family=Open+Sans:wght@400;700&family=Roboto+Mono:wght@600&display=swap">
<style>
  :root {
    --bg: #e4e4e4;
    --paper: #f6f6f6;
    --band-blue: #3f6fa0;
    --band-green: #4ba57a;
    --bar: #333333;
    --ink-light: #ffffff;
    --brand: #1f3f8c;
    --brand-dot: #3d9a4f;
    --fine: #2b3f6e;
  }
  * { box-sizing: border-box; margin: 0; padding: 0; }
  html, body { width: 1200px; height: 1090px; overflow: hidden; background: var(--bg); }
  .canvas { position: relative; width: 1200px; height: 1090px; }

  .carton-top {
    position: absolute; left: 250px; top: 130px; width: 460px; height: 50px;
    background: linear-gradient(90deg, var(--band-blue), var(--band-green));
    display: flex; align-items: center; justify-content: center;
  }
  .carton-top span {
    transform: rotate(180deg);
    font: 300 26px "Encode Sans Condensed", sans-serif; letter-spacing: 3px;
    color: var(--ink-light);
  }

  .side-panel {
    position: absolute; left: 60px; top: 180px; width: 190px; height: 770px;
    background: var(--paper); border-right: 1px solid #dcdcdc;
    padding: 28px 18px; color: var(--fine);
    font: 400 9.5px/1.45 "Open Sans", sans-serif;
  }
  .side-panel h4 { font-weight: 700; font-size: 9.5px; margin-top: 14px; }
  .side-panel h4:first-child { margin-top: 0; }
  .best-before { position: absolute; left: 18px; bottom: 200px; font-weight: 700; font-size: 8.5px; }
  .batch-box {
    position: absolute; left: 18px; bottom: 40px; width: 150px; height: 140px;
    border: 1px solid #6f86b5; border-radius: 10px; padding: 16px 12px;
    display: flex; flex-direction: column; gap: 26px;
  }

  .front-panel {
    position: absolute; left: 250px; top: 180px; width: 460px; height: 770px;
    background: var(--paper);
  }
  .title-band {
    height: 226px; position: relative;
    background: linear-gradient(165deg, var(--band-blue) 0%, #4684a0 45%, var(--band-green) 100%);
  }
  .product-name {
    position: absolute; left: 20px; bottom: 14px;
    font: 300 48px/1 "Encode Sans Condensed", sans-serif; color: var(--ink-light);
    letter-spacing: -0.5px;
  }
  .count-bar {
    display: inline-flex; align-items: center; gap: 12px;
    background: var(--bar); color: var(--ink-light);
    font: 600 14px "Roboto Mono", monospace; letter-spacing: 1px;
    padding: 4px 12px 4px 18px;
  }
  .count-bar .divider { width: 1px; height: 16px; background: var(--ink-light); }
  .brand {
    position: absolute; display: flex; align-items: center; gap: 8px;
    font: 400 20px "Open Sans", sans-serif; color: var(--brand);
  }
  .brand .mark { width: 26px; height: 26px; border-radius: 50%; background: var(--brand-dot); }
  .front-panel .brand { right: 28px; bottom: 34px; }

  .bottle-label {
    position: absolute; left: 770px; top: 340px; width: 370px; height: 470px;
    background: var(--paper); border-radius: 18px; overflow: hidden;
  }
  .bottle-label .title-band { height: 196px; }
  .bottle-label .product-name { font-size: 46px; left: 22px; }
  .bottle-label .brand { right: 22px; bottom: 26px; font-size: 17px; }
  .bottle-label .brand .mark { width: 22px; height: 22px; }
</style>
</head>
<body>
<main class="canvas">
  <div class="carton-top"><span>ANXIETY SUPPORT</span></div>

  <section class="side-panel">
    <h4>Verdant Oakfield</h4>
    <p>Address: Lorem ipsum dolor sit amet, consectetur adipiscing elit, sed do eiusmod tempor incididunt</p>
    <h4>Customer Care:</h4>
    <p>Tel No.: +1-480-555-0142</p>
    <p>Email: care@verdantoakfield.com</p>
    <h4>For more details visit:</h4>
    <p>www.verdantoakfield.com</p>
    <h4>Manufactured by:</h4>
    <p>Address: Lorem ipsum dolor sit amet, consectetur adipiscing elit, sed do eiusmod tempor incididunt</p>
    <p class="best-before">BEST BEFORE 00 MONTHS FROM MANUFACTURE</p>
    <div class="batch-box">
      <span>Batch No. :</span>
      <span>Mfg. Date :</span>
      <span>Cost :</span>
    </div>
  </section>

  <section class="front-panel">
    <div class="title-band"><h1 class="product-name">ANXIETY SUPPORT</h1></div>
    <div class="count-bar"><span>30 CAPSULES</span><span class="divider"></span><span>100gm</span></div>
    <div class="brand"><span class="mark"></span><span>Verdant Oakfield</span></div>
  </section>

  <section class="bottle-label">
    <div class="title-band"><h2 class="product-name">ANXIETY SUPPORT</h2></div>
    <div class="count-bar"><span>30 CAPSULES</span><span class="divider"></span><span>100gm</span></div>
    <div class="brand"><span class="mark"></span><span>Verdant Oakfield</span></div>
  </section>
</main>
</body>
</html>
```